Brightwell Consulting Business Card Design

Business Card Design for Brightwell Consulting. Brightwell Consulting is a boutique consultancy based in Atlanta, GA., that specializes in marketing strategy, organization planning, and leadership development. We provide solutions for small businesses and startups as well as Summit 400 companies.

http://brightwellconsulting.example/

Target Market(s)

We provide solutions for small businesses and startups as well as Summit 400 companies.

Industry/Entity Type

Consulting

Contact Information for Business Card

Two sided business card with priority on contact information, logo, tag line (Inspiration to Dream More, Do More, Become More)

Colors

Designer to choose colors to be used in the design.

Requirements
Must have
• contact information, logo, tag line (Inspiration to Dream More, Do More, Become More)
• Simple no over communication.
Nice to have
• I would like to see different placements of logo and creative use of both sides of the card
Should not have
• Do not put too much information on the card.

```html
<!DOCTYPE html>
<html lang="en">
<head>
<meta charset="utf-8">
<title>Brightwell Consulting Business Card</title>
<link href="https://fonts.googleapis.com/css2?family=Roboto:wght@400;500;700&display=swap" rel="stylesheet">
<style>
  :root {
    --backdrop: #2b2b2b;
    --card-dark: #3a3a3a;
    --card-light: #f6f6f4;
    --ink-dark: #2f2f2f;
    --ink-light: #ffffff;
  }
  * { box-sizing: border-box; margin: 0; padding: 0; }
  html, body {
    width: 799px; height: 1200px; overflow: hidden;
    background: var(--backdrop);
    font-family: "Roboto", Arial, sans-serif;
  }
  .canvas { position: relative; width: 799px; height: 1200px; }
  .card {
    position: absolute; left: 90px; width: 620px; height: 354px;
    border-radius: 22px; overflow: hidden;
  }
  .card--front { top: 140px; background: var(--card-dark); }
  .card--back { top: 700px; background: var(--card-light); }

  .card--front .brand-name {
    position: absolute; left: 0; right: 0; top: 150px;
    text-align: center; color: var(--ink-light);
    font-size: 44px; font-weight: 500; letter-spacing: 1px;
  }

  .card--back .brand-name {
    position: absolute; left: 40px; top: 30px;
    color: var(--ink-dark);
    font-size: 32px; font-weight: 500; letter-spacing: 0.5px;
  }
  .contact { position: absolute; left: 40px; top: 100px; color: var(--ink-dark); }
  .contact__name { font-size: 22px; font-weight: 700; line-height: 26px; margin-bottom: 8px; }
  .contact__line { font-size: 15px; line-height: 20px; }
  .wave {
    position: absolute; left: 0; top: 184px; width: 620px; height: 170px;
  }
  .tagline {
    position: absolute; right: 30px; bottom: 14px;
    color: var(--ink-light); text-align: right;
    font-size: 15px; line-height: 18px;
  }
</style>
</head>
<body>
<main class="canvas">

  <section class="card card--front" aria-label="Card front">
    <p class="brand-name">Brightwell Consulting</p>
  </section>

  <section class="card card--back" aria-label="Card back">
    <p class="brand-name">Brightwell Consulting</p>

    <div class="contact">
      <p class="contact__name">Darnell</p>
      <p class="contact__line">555-014-2290</p>
      <p class="contact__line">darnell@brightwellconsulting.example</p>
      <p class="contact__line">www.brightwellconsulting.example</p>
    </div>

    <svg class="wave" viewBox="0 0 620 170" aria-hidden="true">
      <path d="M0 26 C 120 34, 190 96, 310 100 C 430 104, 530 40, 620 6 L620 170 L0 170 Z" fill="var(--card-dark)"/>
      <path d="M0 40 C 120 48, 190 110, 310 114 C 430 118, 530 54, 620 20 L620 32 C 530 66, 430 130, 310 126 C 190 122, 120 60, 0 52 Z" fill="var(--card-light)"/>
    </svg>

    <p class="tagline">Inspiration to<br>Dream More,<br>Do More,<br>Become More</p>
  </section>

</main>
</body>
</html>
```